Website Design for Gold Buying Company in Australia

We are looking for a Website layout for a company who buy gold pieces from trade and the public.

They would like to communicate that its easy, safe, a great way to make more money, and they pay the best prices in australia for Gold jewelery

Target Market(s)

Adults based in Australia aged 25-60 who are looking to make some extra money

Industry/Entity Type

It Company

Number of Pages Required

2 pages

Requirements
Must have
• Must have a homepage and a page to use for content.

• Will have a feed for the latest Gold, silver and platinum prices they are buying and selling at.

• Needs to have a from on the homepage where people can submit their details to be sent a ''Nugget Box'' which allows them to send gold pieces to eb valued and bought by the company.

Nice to have
• Would be nice to have a steped out graphic of how the ''Nugget Box by mail'' process works [Request a Kit, Send in your Gold, We Value and grade it, We pay you cash, cheque of Direct Deposit]

• Imagery will be gold related

• Colour schemes are not a major Issue-but using some gold or silver would be a good idea
Should not have
• No cheesy gold graphics please :)

```html
<!DOCTYPE html>
<html lang="en">
<head>
<meta charset="utf-8">
<title>Aurumhaus.com.au – Best prices in Australia</title>
<link rel="stylesheet" href="https://fonts.googleapis.com/css2?family=Arimo:wght@400;700&family=Lora:ital,wght@0,400;0,700;1,400;1,700&display=swap">
<style>
:root{
  --topline:#7d7b76;
  --cream-top:#ffffff;
  --cream-bottom:#f8ebc4;
  --nav-top:#b08f42;
  --nav-bottom:#8d6f2c;
  --nav-active:#e7bd52;
  --grey-text:#8a8782;
  --tan-top:#b39f80;
  --tan-bottom:#d7c3a0;
  --panel-head:#f4f0ea;
  --field-bg:#f6f3ee;
  --field-border:#c9c2b6;
  --price:#a67c1c;
  --label:#7d7a74;
  --kit-head:#8b8781;
  --kit-body:#79766f;
  --kit-gold:#f3d27a;
  --send:#e0b23a;
  --foot-top:#b88f25;
  --foot-bottom:#d4a93a;
  --foot-line:#8a6d27;
  --foot-link:#6d5316;
}
*{box-sizing:border-box;margin:0;padding:0}
html,body{width:1200px;height:550px;overflow:hidden;background:#fff}
body{position:relative;font-family:"Arimo",Arial,sans-serif}
.abs{position:absolute}

.top-line{left:0;top:0;width:1200px;height:6px;background:var(--topline)}
.masthead{left:0;top:6px;width:1200px;height:66px;background:linear-gradient(var(--cream-top),var(--cream-bottom));border-bottom:1px solid #d8c58f}
.brand{left:235px;top:20px;font-family:"Lora",Georgia,serif;font-weight:700;font-size:30px;color:#6f6c66;letter-spacing:-.5px}
.brand-divider{left:544px;top:29px;width:1px;height:24px;background:#d3c8ae}
.tagline{left:557px;top:30px;font-family:"Lora",Georgia,serif;font-style:italic;font-size:16px;color:#a9a496}
.search{left:766px;top:28px;width:166px;height:23px;border:1px solid #d2cfc6;background:#fff;font-size:10px;color:#777;padding:5px 6px}
.search-icon{left:936px;top:30px}

.nav{left:0;top:72px;width:1200px;height:34px;background:linear-gradient(var(--nav-top),var(--nav-bottom));border-bottom:1px solid #7a6228}
.nav a{position:absolute;top:10px;color:#fff;font-size:12.5px;text-decoration:none;white-space:nowrap}
.nav a.active{top:1px;height:32px;padding:9px 10px 0;background:var(--nav-active)}

.rates{left:233px;top:122px;width:477px;height:285px;background:linear-gradient(var(--tan-top),var(--tan-bottom))}
.rates-card{left:14px;top:14px;width:448px;height:258px;background:#fff;border:1px solid #bfae90}
.rates-head{left:0;top:0;width:446px;height:36px;background:var(--panel-head);border-bottom:1px solid #cfc5b5}
.rates-title{left:11px;top:2px;font-family:"Lora",Georgia,serif;font-size:27px;color:#8f8b84}
.rates-title b{font-style:italic;color:#6d6a64}
.metal{position:absolute;top:48px;width:130px}
.metal h3{font-family:"Lora",Georgia,serif;font-style:italic;font-weight:400;font-size:21px;color:#9a968f}
.bar{width:112px;height:64px;margin:6px 0 0 8px;border-radius:4px}
.bar.gold{background:linear-gradient(160deg,#fff1a0,#e6b72a 55%,#c99710)}
.bar.platinum{background:linear-gradient(160deg,#ffffff,#dadada 55%,#b8b8b8)}
.bar.silver{background:linear-gradient(160deg,#f2f2f2,#a9a9a9 55%,#7c7c7c)}
.metal .label{font-size:10px;font-weight:700;color:var(--label);margin-top:13px}
.metal .price{width:127px;height:25px;margin-top:5px;background:var(--field-bg);border:1px solid var(--field-border);color:var(--price);font-size:13px;padding:4px 6px}
.metal .label.sell{margin-top:14px}
.col-rule{top:49px;width:1px;height:195px;background:#e1dbd0}

.kit{left:725px;top:122px;width:231px;height:285px;background:var(--kit-body)}
.kit-head{left:0;top:0;width:231px;height:50px;background:var(--kit-head);border-bottom:1px solid #6e6b65}
.kit-title{left:11px;top:3px;font-family:"Lora",Georgia,serif;font-style:italic;font-weight:700;font-size:33px;color:var(--kit-gold)}
.kit-lead{left:13px;top:63px;font-size:13px;color:var(--kit-gold)}
.kit-copy{left:13px;top:95px;width:206px;font-size:10px;line-height:15px;color:#f4f1ea}
.kit-label{left:14px;font-size:10px;font-weight:700;color:#e2ded6}
.kit-field{left:13px;width:202px;height:21px;background:#fffcf4;border:1px solid #ccc6b8;font-size:9px;color:#555;padding:5px 6px}
.send{left:165px;top:249px;width:50px;height:20px;background:linear-gradient(#f0c858,var(--send));border:1px solid #c49a2c;font-family:"Lora",Georgia,serif;font-style:italic;font-weight:700;font-size:11px;color:#6d5316;text-align:center;line-height:18px}

.footer{left:233px;top:460px;width:723px;height:50px;background:linear-gradient(var(--foot-top) 0,var(--foot-top) 50%,var(--foot-bottom) 50%);border-bottom:5px solid var(--foot-line)}
.footer-links{left:0;top:30px;width:723px;text-align:center;font-size:8.5px;color:var(--foot-link)}
.footer-links span{margin:0 7px}
.footer-url{left:233px;top:516px;width:723px;text-align:center;font-family:"Lora",Georgia,serif;font-weight:700;font-size:18px;color:#b39a62}
</style>
</head>
<body>
<div class="abs top-line"></div>
<header class="abs masthead"></header>
<div class="abs brand">Aurumhaus.com.au</div>
<div class="abs brand-divider"></div>
<div class="abs tagline">Best prices in Australia</div>
<div class="abs search">Search</div>
<svg class="abs search-icon" width="18" height="18" viewBox="0 0 18 18" aria-label="Search">
  <circle cx="7" cy="7" r="5" fill="#eef3f7" stroke="#8a8a8a" stroke-width="2"/>
  <line x1="11" y1="11" x2="16" y2="16" stroke="#9a7a3a" stroke-width="3" stroke-linecap="round"/>
</svg>

<nav class="abs nav">
  <a style="left:244px">About Us</a>
  <a style="left:321px">What we Buy &amp; Sell</a>
  <a style="left:460px">How it works</a>
  <a style="left:563px">Commen Questions</a>
  <a style="left:701px">Bullion</a>
  <a style="left:764px">Contact Us</a>
  <a class="active" style="left:842px">Trade enquires</a>
</nav>

<section class="abs rates">
  <div class="abs rates-card">
    <div class="abs rates-head"><div class="abs rates-title"><b>Current</b> Rates</div></div>
    <div class="abs col-rule" style="left:149px"></div>
    <div class="abs col-rule" style="left:297px"></div>
    <div class="metal" style="left:11px">
      <h3>Gold</h3>
      <div class="bar gold" role="img" aria-label="Gold bullion bar"></div>
      <div class="label">Buying</div><div class="price">$32.3292/gg</div>
      <div class="label sell">Selling</div><div class="price">$1,005.50/oz</div>
    </div>
    <div class="metal" style="left:159px">
      <h3>Platinum</h3>
      <div class="bar platinum" role="img" aria-label="Platinum bullion bar"></div>
      <div class="label">Buying</div><div class="price">$32.3292/gg</div>
      <div class="label sell">Selling</div><div class="price">$1,005.50/oz</div>
    </div>
    <div class="metal" style="left:308px">
      <h3>Silver</h3>
      <div class="bar silver" role="img" aria-label="Silver bullion bar"></div>
      <div class="label">Buying</div><div class="price">$32.3292/gg</div>
      <div class="label sell">Selling</div><div class="price">$1,005.50/oz</div>
    </div>
  </div>
</section>

<aside class="abs kit">
  <div class="abs kit-head"><div class="abs kit-title">Nugget Box</div></div>
  <div class="abs kit-lead">Request a Kit, Send in your Gold</div>
  <p class="abs kit-copy">We Value and grade it, We pay you cash, cheque of Direct Deposit.</p>
  <div class="abs kit-label" style="top:143px">Name</div>
  <div class="abs kit-field" style="top:157px">Mara Elwood</div>
  <div class="abs kit-label" style="top:193px">E-mail</div>
  <div class="abs kit-field" style="top:207px">mara.elwood@example.com</div>
  <div class="abs send">Send »</div>
</aside>

<footer class="abs footer">
  <div class="abs footer-links"><span>About Us</span><span>What we Buy &amp; Sell</span><span>How it works</span><span>Commen Questions</span><span>Bullion</span><span>Contact Us</span><span>Trade enquires</span></div>
</footer>
<div class="abs footer-url">www.aurumhaus.com.au</div>
</body>
</html>
```